Harborvale Ventures brochure for Investment partnership, young harold pembly

We need a brochure design to attract new investors for our investing partnership Called Harborvale Ventures. We are based in New Orleans, La. We primarily invest in stocks, bonds, and crypto but venture out into other categories as well. We would like to see designs with the black and gold like our logo. The final design should say new, fresh, sleek, tech, and honorable. BROUCHURE WILL BE 4 pages.or one folded sheet a paparer if that makes sense.
Updates

A chart showing Harborvale Ventures gains since 2019 28.6 percent and the TR 400 gAINS 7.1 PERCENT

Target Market(s)

Probable Investors

Industry/Entity Type

Financial Planning

Colors

Designer to choose only greyscale colors for use in the design.

Requirements
Must have
• Black and Gold accent. Stock market feel. Sleek, High tech, innovative, Intellgent design.
Nice to have
• Page colors possibly black.
Should not have
• Boring, Old school,

```html
<!DOCTYPE html>
<html lang="en">
<head>
<meta charset="utf-8">
<title>Harborvale Ventures – Brochure</title>
<link href="https://fonts.googleapis.com/css2?family=Marcellus+SC&family=Oswald:wght@600&display=swap" rel="stylesheet">
<style>
  :root {
    --gold: #dfbf3e;
    --gold-text: #d9b53b;
    --black: #000000;
    --white: #f2f2f2;
    --canvas: #ffffff;
    --photo-light: #9a9a9a;
    --photo-dark: #1c1c1c;
  }
  * { margin: 0; padding: 0; box-sizing: border-box; }
  html, body { width: 1200px; height: 960px; overflow: hidden; background: var(--canvas); }
  body { position: relative; font-family: "Marcellus SC", serif; }

  .masthead {
    position: absolute; top: 28px; left: 0; width: 1200px;
    text-align: center; color: var(--black);
  }
  .masthead .brand-name { font-size: 44px; letter-spacing: 1px; line-height: 1; }
  .masthead .brand-rule { width: 330px; height: 2px; background: var(--black); margin: 12px auto 0; }

  .page {
    position: absolute; top: 158px; width: 279px; height: 720px;
    background: var(--black); color: var(--white); text-align: center; overflow: hidden;
  }
  .page-1 { left: 13px; }
  .page-2 { left: 311px; }
  .page-3 { left: 610px; }
  .page-4 { left: 909px; }

  .band { position: absolute; left: 0; width: 100%; background: var(--gold); }
  .band-top { top: 0; }
  .band-bottom { bottom: 0; }

  .wordmark { color: var(--gold-text); letter-spacing: .5px; line-height: 1; }
  .wordmark.on-gold { color: var(--black); }

  .block { position: absolute; left: 0; width: 100%; padding: 0 14px; }

  .label {
    position: absolute; top: 886px; width: 279px; text-align: center;
    font-family: "Oswald", sans-serif; font-weight: 600; font-size: 29px; color: var(--black);
    transform: scaleX(.82);
  }

  /* Page 1 */
  .cover-photo {
    position: absolute; top: 33px; left: 0; width: 100%; height: 326px;
    background: linear-gradient(180deg, var(--photo-light) 0%, #5a5a5a 45%, var(--photo-dark) 85%, var(--black) 100%);
  }
  .lead { font-size: 16px; line-height: 27px; }

  /* Page 3 */
  .steps-text { font-size: 11.6px; line-height: 14.5px; }
  .icon { position: absolute; left: 50%; transform: translateX(-50%); }
</style>
</head>
<body>

<header class="masthead">
  <div class="brand-name">Harborvale Ventures</div>
  <div class="brand-rule"></div>
</header>

<!-- Page 1: cover -->
<section class="page page-1">
  <div class="band band-top" style="height:33px"></div>
  <div class="cover-photo" role="img" aria-label="Black and white photograph of a domed classical building at the end of a narrow city street"></div>
  <p class="block lead" style="top:374px">Become a partner and build generational wealth by investing in the stock market</p>
  <p class="block lead" style="top:538px">A first of its kind<br>Investment Club</p>
  <div class="block wordmark" style="top:648px;font-size:20px">Harborvale Ventures</div>
</section>

<!-- Page 2: invitation -->
<section class="page page-2">
  <div class="band band-top" style="height:33px"></div>
  <p class="block lead" style="top:156px">If you are receiving this brochure its because someone sees you as a person that doesn't want to just work and pay bills.</p>
  <p class="block lead" style="top:345px">Your someone who wants to build real generational wealth.</p>
  <p class="block lead" style="top:453px">Not throw schemes but the using the greatest wealth builder available. The stock market.</p>
  <div class="band band-bottom" style="height:56px">
    <div class="wordmark on-gold" style="margin-top:20px;font-size:13px">Harborvale Ventures</div>
  </div>
</section>

<!-- Page 3: how it works -->
<section class="page page-3">
  <div class="band band-top" style="height:62px">
    <div class="wordmark on-gold" style="margin-top:25px;font-size:13px">Harborvale Ventures</div>
  </div>

  <svg class="icon" style="top:94px" width="36" height="38" viewBox="0 0 36 38" aria-hidden="true">
    <rect x="7" y="5" width="27" height="32" fill="#b8951f"/>
    <rect x="2" y="1" width="27" height="32" fill="var(--gold)"/>
    <g stroke="#000" stroke-width="1.6"><line x1="7" y1="8" x2="24" y2="8"/><line x1="7" y1="13" x2="24" y2="13"/><line x1="7" y1="18" x2="24" y2="18"/><line x1="7" y1="23" x2="24" y2="23"/></g>
  </svg>
  <p class="block" style="top:148px;font-size:14.5px">How it works</p>

  <svg class="icon" style="top:168px" width="42" height="40" viewBox="0 0 42 40" aria-hidden="true">
    <path d="M2 16 L21 2 L40 16 V38 H2 Z" fill="var(--gold)"/>
    <rect x="9" y="7" width="24" height="20" fill="#fff3c4"/>
    <path d="M2 16 L21 30 L40 16 V38 H2 Z" fill="#e8c94a" stroke="#000" stroke-width="1"/>
    <text x="21" y="22" text-anchor="middle" font-size="14" font-family="Oswald, sans-serif" fill="#000">$</text>
  </svg>
  <p class="block steps-text" style="top:220px">Make initial deposit. The general partner will invest in stocks, bonds and other investment vehicles on your behalf.</p>

  <svg class="icon" style="top:284px" width="42" height="40" viewBox="0 0 42 40" aria-hidden="true">
    <circle cx="17" cy="17" r="14" fill="none" stroke="var(--gold)" stroke-width="5" stroke-dasharray="4 3"/>
    <circle cx="17" cy="17" r="11" fill="var(--gold)"/>
    <text x="17" y="23" text-anchor="middle" font-size="16" font-family="Oswald, sans-serif" fill="#000">$</text>
    <circle cx="33" cy="31" r="6" fill="none" stroke="var(--gold)" stroke-width="3"/>
  </svg>
  <p class="block steps-text" style="top:336px">There is no upfront fees. The general partner will guarantee a 5 percent return and will work for free on your behalf until that is achieved. After the 5 percent return on the dollars invested the limited partner will receive 80 percent and the general partner will receive 20 percent of every dollar gained.</p>

  <svg class="icon" style="top:486px" width="36" height="44" viewBox="0 0 36 44" aria-hidden="true">
    <path d="M11 2 H25 L21 10 H15 Z" fill="var(--gold)"/>
    <path d="M14 12 H22 C34 20 36 42 18 42 C0 42 2 20 14 12 Z" fill="var(--gold)"/>
    <text x="18" y="35" text-anchor="middle" font-size="18" font-family="Oswald, sans-serif" fill="#000">$</text>
  </svg>
  <p class="block steps-text" style="top:540px">As the return and investments multiply the interests begins to compound annually. The legal partner legally owns shares of stock within the club and may redeem once a year or let money continue to earn interest.</p>

  <svg class="icon" style="top:654px" width="42" height="40" viewBox="0 0 42 40" aria-hidden="true">
    <path d="M6 20 A15 15 0 0 1 33 11" fill="none" stroke="var(--gold)" stroke-width="3"/>
    <path d="M36 20 A15 15 0 0 1 9 29" fill="none" stroke="var(--gold)" stroke-width="3"/>
    <path d="M28 6 L36 10 L30 16 Z" fill="var(--gold)"/>
    <path d="M14 34 L6 30 L12 24 Z" fill="var(--gold)"/>
    <text x="21" y="28" text-anchor="middle" font-size="20" font-family="Oswald, sans-serif" fill="var(--gold)">$</text>
  </svg>
</section>

<!-- Page 4: about -->
<section class="page page-4">
  <div class="block wordmark" style="top:62px;font-size:27px;line-height:32px">Harborvale Ventures</div>
  <p class="block" style="top:172px;font-size:14px;line-height:27px;color:var(--gold-text)">About Harborvale Ventures and General Partner</p>
  <p class="block" style="top:252px;font-size:13px;line-height:27px">Harborvale Ventures was founded in 2019 by General Partner Dorian Mercer Jr with a group economic empowerment mission. Dorian Mercer has invested int stocks since a teenager received his BA in ecomics from Crescent Bay University and is currently attending the University of Pinewood.</p>
  <div class="band band-bottom" style="height:121px">
    <div class="wordmark on-gold" style="margin-top:54px;font-size:13px">Harborvale Ventures</div>
  </div>
</section>

<div class="label" style="left:13px">PAGE 1</div>
<div class="label" style="left:311px">PAGE 2</div>
<div class="label" style="left:610px">PAGE 3</div>
<div class="label" style="left:909px">PAGE 4</div>

</body>
</html>
```